Australian Conference Brochure

I would like to have a 4 page A4 brochure made up , the product is a service which builds digital libraries for hospital medical equipment instruction manuals ( www.medirostrasystems.com.au and www.wardgearhandbookvaultonline.com )

I have attached content and order of the brochure to this project ( note pages are mixed up ) the 4th page is attached separately in pdf as it my logo .

The feel for the first page must be along the lines of this link :

http://www.carewellstandards.example.au/wp-content/uploads/2012/03/0.842.gif

The heading must be pronounced and jump out at you

Pages 2 and 3 must have the same feel as the medirostra systems website

The screen shots of the library can be accessed via the library – I can give you access to it for those

The 4 page must be a sketched version of the desktop computer ( see attached pdf ) with 3 instructions manuals coming out of it , with titles :
ICU Ventilator Manufacturers User Troubleshooting Guide
Patient Lift Hoist Manufacturers Set-up Instructions
Diathermy Manufacturers Clinicians Directions for Use
The company logo can be on this page with a info@medirostrasystems.com.au e-mail address

```html
<!DOCTYPE html>
<html lang="en">
<head>
<meta charset="utf-8">
<title>Medirostra Systems – Conference Brochure</title>
<link href="https://fonts.googleapis.com/css2?family=PT+Sans:ital,wght@0,400;0,700;1,400&family=PT+Sans+Narrow:wght@400;700&display=swap" rel="stylesheet">
<style>
:root{
  --stage:#e7e5e1;
  --paper:#ffffff;
  --blue:#2b8dc5;
  --blue-deep:#1b6aa4;
  --blue-ink:#1d5f95;
  --navy:#123f66;
  --orange:#f08b1c;
  --red:#d8271e;
  --ink:#3b3b3b;
  --muted:#6c6c6c;
  --panel-top:#f3f3f3;
  --panel-bottom:#c9cacc;
  --box:#ffffff;
  --screen:#d9e3ec;
}
*{box-sizing:border-box;margin:0;padding:0}
html,body{width:909px;height:1200px;overflow:hidden}
body{background:var(--stage);font-family:"PT Sans",Arial,sans-serif;color:var(--ink);position:relative}

.spread{position:absolute;left:83px;width:766px;height:530px;background:var(--paper);box-shadow:0 2px 8px rgba(0,0,0,.25);overflow:hidden}
.spread--outer{top:47px}
.spread--inner{top:644px}
.page{position:absolute;top:0;width:383px;height:530px}
.page--left{left:0}
.page--right{left:383px}
.abs{position:absolute}

/* type */
.body-text{font-size:6.3px;line-height:1.38;color:var(--ink)}
.body-text p{margin-bottom:5px}
.sub-head{color:var(--blue-ink);font-weight:700;font-size:7px;line-height:1.25;margin:6px 0 3px}
.url{font-size:6px;letter-spacing:1.4px;color:var(--muted);text-transform:lowercase}

/* band */
.band{background:var(--blue);color:#fff;font-weight:700;font-size:9px;display:flex;align-items:center;justify-content:center}

/* brand */
.brand{display:flex;align-items:center;gap:5px;color:var(--blue-deep);font-weight:700;font-size:11px;letter-spacing:.2px}
.brand__dot{width:12px;height:12px;background:var(--blue-deep)}
.brand--light{color:#fff}
.brand--light .brand__dot{background:#fff}

/* page 4 */
.hero-art{left:11px;top:7px;width:206px;height:133px;background:linear-gradient(160deg,#cfd6dd,#8e98a3 60%,#c7ccd2)}
.hero-title{left:110px;top:12px;width:220px;font-weight:700;font-size:17px;line-height:1.05;color:var(--navy);font-family:"PT Sans Narrow","PT Sans",sans-serif}
.hero-title em{font-style:normal;color:var(--red)}
.hero-sub{left:185px;top:44px;width:160px;font-size:8px;line-height:1.25;color:var(--blue-ink);text-align:center}
.hero-sub b{color:var(--blue-deep)}
.help-badge{left:261px;top:82px;width:86px;height:70px;text-align:center;color:var(--blue-deep);font-weight:700}
.help-badge__word{display:inline-block;background:var(--blue);color:#fff;font-size:16px;padding:1px 8px;letter-spacing:1px;border-radius:2px}
.help-badge__line{font-size:11px;line-height:1.05;margin-top:3px}

/* page 1 */
.cover{background:var(--blue)}
.cover-head{left:20px;top:18px;width:343px;text-align:center;color:#fff;font-weight:700;font-size:8.6px;line-height:1.35}
.standards-panel{left:23px;top:73px;width:353px;height:330px;background:linear-gradient(180deg,var(--panel-top),var(--panel-bottom));border-radius:3px}
.standards-tag{left:106px;top:34px;width:144px;height:33px;background:var(--orange);color:#fff;font-weight:700;font-size:6.6px;text-align:center;display:flex;align-items:center;justify-content:center;line-height:1.25;border:1px solid #fff}
.std-box{background:var(--box);border:1px solid #bbb;font-size:5.4px;line-height:1.35;padding:5px 6px;color:var(--ink)}
.std-box h4{font-size:6.2px;line-height:1.25;color:#222;margin-bottom:4px}
.std-box .std-sub{font-weight:700;font-size:5.8px;margin:4px 0 2px}
.std-box--head{background:#e7e7e7}
.arrow-layer{left:0;top:0;width:353px;height:330px;pointer-events:none}

/* page 2 */
.lead{color:var(--blue-ink);font-weight:700;font-size:8.2px;line-height:1.25;margin-bottom:6px}
.flag{width:60px;height:32px;background:linear-gradient(135deg,#1f3f8f,#2c56ad);margin:6px auto}
.shot{background:#fff;border:1px solid #c9c9c9;box-shadow:0 1px 2px rgba(0,0,0,.15)}
.shot__bar{height:8px;background:var(--screen);border-bottom:1px solid #c4ccd4;font-size:4.6px;padding:1px 3px;color:#555}
.shot__row{height:4px;margin:4px 5px;background:#e9edf1}
.shot__btn{position:absolute;right:6px;width:34px;height:8px;border:1px solid #9bb;background:#f2f6f9}
.shot__mark{position:absolute;right:8px;bottom:6px;width:24px;height:8px;background:var(--blue)}
.doc-preview{background:#fff;border:1px solid #c9c9c9;font-size:5px;line-height:1.3;padding:6px;color:#444}
.doc-preview table{width:100%;border-collapse:collapse;margin-top:4px}
.doc-preview td{border:1px solid #999;height:7px;padding:0 2px;font-size:4.4px}
.doc-preview h5{font-size:9px;color:#222;margin-bottom:3px}

/* page 3 */
.benefits{left:211px;top:16px;width:162px;height:297px;background:var(--blue);color:#fff;padding:9px 8px}
.benefits h3{font-size:10.5px;line-height:1.12;text-align:center;margin-bottom:8px;border-bottom:1px solid rgba(255,255,255,.5);padding-bottom:6px}
.benefits ul{list-style:none;font-size:5.9px;line-height:1.35}
.benefits li{margin-bottom:6px;padding-left:10px;position:relative}
.benefits li::before{content:"";position:absolute;left:0;top:1px;width:6px;height:6px;background:#fff;border-radius:1px}
.benefits li::after{content:"";position:absolute;left:1.5px;top:2px;width:2px;height:3px;border:solid var(--blue);border-width:0 1px 1px 0;transform:rotate(45deg)}
.cycle-box{background:#fff;border:1px solid #bbb;border-radius:6px;font-size:5.4px;line-height:1.3;text-align:center;padding:4px;display:flex;align-items:center;justify-content:center;box-shadow:0 1px 2px rgba(0,0,0,.2)}
.foot-band{left:16px;top:483px;width:360px;height:40px;background:var(--blue);color:#fff;font-size:5.6px;line-height:1.35;text-align:center;display:flex;align-items:center;justify-content:center;padding:0 12px}
.ticklist{list-style:none}
.ticklist li{position:relative;padding-left:9px;margin-bottom:3px}
.ticklist li::before{content:"";position:absolute;left:0;top:1px;width:5px;height:5px;background:var(--blue)}
</style>
</head>
<body>

<!-- Outer spread: back cover (page 4) and front cover (page 1) -->
<section class="spread spread--outer">

  <div class="page page--left">
    <div class="abs hero-art" role="img" aria-label="Sketched desktop computer with three instruction manuals coming out of the screen"></div>
    <h1 class="abs hero-title">Where the <em>hell</em> is the user manual?!</h1>
    <p class="abs hero-sub">…in the <b>Ward Gear Handbook Vault</b><br>of course!</p>
    <div class="abs help-badge">
      <span class="help-badge__word">HELP</span>
      <p class="help-badge__line">24/7-365<br>NO EXCUSES!</p>
    </div>

    <div class="abs band" style="left:0;top:167px;width:383px;height:24px">Currently used by more than 200 hospitals, including...</div>

    <div class="abs body-text" style="left:17px;top:200px;width:158px">
      <p class="sub-head" style="margin-top:0">CQSA Clinical Indicator User Manual 2012 Intensive Care version 4</p>
      <p>7.2: ICU Library facilities – an appropriate range of bench manuals, textbooks, journals and access to electronic medical information should be available 24 hours a day within the unit complex.</p>
      <p>8.1 Protocols and in-service training for medical and nursing staff need to be available for the use of all equipment, including steps to be taken in event of a malfunction</p>
      <p class="sub-head">PNRA : RECOMMENDED PRACTICES</p>
      <p>RP for Electrosurgery 2.8 March 2012</p>
      <p>Read and attach the manufacturer's manual to the unit or cart on which the ESU sits (pg 275)</p>
      <p>During the use of AEC ( Anyon estimated coagulation technology ) all manufacturers written instructions should be followed in addition to all safety measures for monopolar surgery.</p>
      <p class="sub-head">Southern College of Anaesthesia Practice (SCAP)</p>
      <p>PS 31BP 2012 Guidelines on Checking Anaesthesia Delivery Systems</p>
    </div>

    <div class="abs body-text" style="left:190px;top:200px;width:175px">
      <p>It is the responsibility of each facility to ensure that specific checklists are available in accordance with manufacturers' guidelines, for each item of equipment relevant to anaesthesia delivery systems.</p>
      <p class="sub-head">TS/NS 4173:2004 Guide to the safe use of lasers in health care</p>
      <p>SECTION 9 SAFE PRACTICES</p>
      <p>9.2 (j) The laser safety rules and equipment instructions are required to be made available at the site of use.</p>
      <p class="sub-head">Trans-Tasman Resuscitation Board Guideline 11.4 Dec 2010</p>
      <p>Electrical Therapy for adult advanced life support</p>
      <p>Care should be taken to ensure that the pads or electrodes are applied in accordance with the manufacturer's instructions.</p>
      <p class="sub-head">STATE CORONER EASTLAND</p>
      <p>Coroner's "Investigation Standard": Fall-related deaths in hospital</p>
      <p>Relevant Equipment or work practice ( pages 2 )</p>
      <p>By if a particular product was involved, were the manufacturer's instructions available and followed? (If not why not?).</p>
    </div>

    <div class="abs brand" style="left:17px;top:452px"><span class="brand__dot"></span>medirostra systems</div>
    <p class="abs url" style="left:230px;top:482px">www.medirostrasystems.com.au</p>
  </div>

  <div class="page page--right cover">
    <p class="abs cover-head">Every Hospital in Australia and New Zealand has a legal and compliance obligation to make sure all Clinical Staff can access the Manufacturer's Instructions for Use for equipment they use every day</p>

    <div class="abs standards-panel">
      <div class="abs standards-tag">NATIONAL CARE QUALITY SERVICE<br>(NCQS) STANDARDS</div>

      <div class="abs std-box std-box--head" style="left:4px;top:78px;width:152px;height:36px">
        <h4>CQSA CarePlusNational Guidelines – Guideline 15 Corporate Systems and Safety</h4>
      </div>
      <div class="abs std-box" style="left:4px;top:116px;width:152px;height:92px">
        <h4>Criterion 15.15.1</h4>
        <p>" ....An organisation should have documented management strategies for all medical devices used within its facilities including:</p>
        <p>• medical devices owned, leased or loaned by the organisation etc. ......"</p>
        <p style="margin-top:3px">TS/NS 3551:2004 Technical management programs for medical devices? details for the organisation's board, executives and managers the minimum requirements of an effective strategy for the management of medical devices ....."</p>
      </div>

      <div class="abs std-box" style="left:164px;top:78px;width:186px;height:108px">
        <h4>National Care Quality Service Standard 3</h4>
        <p>3.16 Reprocessing reusable medical equipment, instruments and devices in accordance with relevant national or international standards and manufacturers' instructions</p>
        <h4 style="margin-top:6px">National Care Quality Service Standard 8</h4>
        <p class="std-sub">8.4 Key task : Outputs of improvement processes may include :</p>
        <p>procedures, protocols and guidelines for the use of and access to equipment</p>
      </div>

      <div class="abs std-box" style="left:4px;top:222px;width:166px;height:102px">
        <h4>TS/NS 3551:2004</h4>
        <p class="std-sub">SECTION 2 MEDICAL DEVICE MANAGEMENT PROGRAM</p>
        <p class="std-sub">2.3.6.4 Device-specific documents</p>
        <p>Documents such as technical and user manuals shall be identified and their location recorded in the database.</p>
      </div>
      <div class="abs std-box" style="left:176px;top:222px;width:174px;height:102px">
        <h4>TS/NS 3551:2012</h4>
        <p class="std-sub">SECTION 2 MEDICAL DEVICE MANAGEMENT PROGRAM</p>
        <p class="std-sub">2.4.3 2.4.3 Supporting documentation</p>
        <p>Documents such as standards, user guides, technical manuals and other supporting publications shall be identified, stored, issued and updated in a controlled manner.</p>
      </div>

      <svg class="abs arrow-layer" viewBox="0 0 353 330" aria-hidden="true">
        <defs><marker id="tipOrange" markerWidth="6" markerHeight="6" refX="3" refY="3" orient="auto"><path d="M0,0 L6,3 L0,6 z" fill="#f08b1c"/></marker></defs>
        <g stroke="#f08b1c" stroke-width="2.4" fill="none" marker-end="url(#tipOrange)">
          <path d="M130,62 C110,70 95,70 82,76"/>
          <path d="M226,62 C240,68 250,70 258,76"/>
          <path d="M176,68 C180,130 110,190 95,218"/>
          <path d="M190,68 C196,130 250,190 262,218"/>
        </g>
      </svg>
    </div>

    <div class="abs brand brand--light" style="left:114px;top:434px;font-size:13px"><span class="brand__dot"></span>medirostra systems</div>
    <p class="abs url" style="left:0;top:482px;width:383px;text-align:center;color:#e4f1fa">www.medirostrasystems.com.au</p>
  </div>
</section>

<!-- Inner spread: page 2 and page 3 -->
<section class="spread spread--inner">

  <div class="page page--left">
    <div class="abs band" style="left:0;top:11px;width:383px;height:22px">Currently used by more than 200 hospitals, including...</div>

    <div class="abs body-text" style="left:16px;top:48px;width:177px">
      <p class="lead">Accreditation has been a significant contributor to driving and inspiring continuous quality improvements within healthcare.</p>
      <p>Standardisation has a proven track record within large complex systems and healthcare is no exception.</p>
      <p>One of the benefits of the new National Care Quality Service Standards is that it will continue to drive proven and tested strategies which inevitably become standards.</p>
      <p>The Ward Gear Handbook Vault ( WGHV ) has entered its 10th year as the single access point for all New South Wales hospitals to access the medical equipment instruction manuals.</p>
      <p class="lead">We have standardized access to over 220 Australian and UK Hospitals, and we would like your support to roll this out to all Australian Hospitals.</p>
      <p>Nursing Staff , Clinicians and other professional Medical Equipment Users should be able to walk up to any PC in any hospital in Australia and get the Manufacturer's Reference Documentation ( Instructions for Use , Set-up Guides , User Manuals ) within a few clicks ........</p>
      <p>Just like they do with Chemicals and their MSDS.</p>
      <div class="flag" role="img" aria-label="Australian national flag"></div>
      <p style="text-align:center;color:var(--blue-ink)">info@medirostrasystems.com.au</p>
      <p style="margin-top:6px">Made by Australians , Employing Australians , Supporting Australian Healthcare</p>
    </div>

    <div class="abs shot" style="left:200px;top:36px;width:177px;height:88px">
      <div class="shot__bar">Ward Gear Handbook Vault</div>
      <div class="shot__row" style="width:60%"></div>
      <div class="shot__row" style="width:45%"></div>
      <span class="shot__btn" style="top:16px"></span><span class="shot__btn" style="top:36px"></span><span class="shot__btn" style="top:56px"></span>
      <span class="shot__mark"></span>
    </div>
    <div class="abs shot" style="left:200px;top:130px;width:177px;height:88px">
      <div class="shot__bar">Ward Gear Handbook Vault</div>
      <div class="shot__row" style="width:55%"></div>
      <div class="shot__row" style="width:40%"></div>
      <span class="shot__btn" style="top:16px"></span><span class="shot__btn" style="top:36px"></span><span class="shot__btn" style="top:56px"></span>
      <span class="shot__mark"></span>
    </div>
    <div class="abs shot" style="left:200px;top:224px;width:177px;height:92px">
      <div class="shot__bar">Ward Gear Handbook Vault</div>
      <div class="shot__row" style="width:62%"></div>
      <div class="shot__row" style="width:58%"></div>
      <div class="shot__row" style="width:60%"></div>
      <div class="shot__row" style="width:52%"></div>
      <div class="shot__row" style="width:57%"></div>
      <span class="shot__mark"></span>
    </div>
    <div class="abs doc-preview" style="left:200px;top:328px;width:177px;height:54px">
      <p>The page at www.wardgearhandbookvaultonline.com says:</p>
      <p style="margin-top:3px">I agree to the terms and conditions of the Ward Gear Handbook Vault and will read the manual before first use of this device.</p>
      <p style="text-align:right;margin-top:4px"><span style="border:1px solid #888;padding:0 6px">OK</span> <span style="border:1px solid #888;padding:0 4px">Cancel</span></p>
    </div>

    <div class="abs doc-preview" style="left:17px;top:409px;width:174px;height:114px">
      <p style="display:flex;justify-content:space-between"><b>Appendix A</b><span>Section 5</span></p>
      <p style="margin-top:4px"><b>A.1 Troubleshooting guide</b></p>
      <p>Use this table to find the likely cause of a fault and the steps to clear it before calling service.</p>
      <table>
        <tr><td>Alarm</td><td>Possible cause</td><td>Action</td></tr>
        <tr><td>Low pressure</td><td>Circuit leak</td><td>Check seals</td></tr>
        <tr><td>High pressure</td><td>Blocked tube</td><td>Clear circuit</td></tr>
        <tr><td>Power fail</td><td>Mains lost</td><td>Check supply</td></tr>
        <tr><td>Sensor error</td><td>Loose cable</td><td>Reconnect</td></tr>
      </table>
    </div>
    <div class="abs doc-preview" style="left:204px;top:404px;width:173px;height:112px">
      <h5>Troubleshooting</h5>
      <table>
        <tr><td style="width:30%">Problem</td><td>Possible Solution</td></tr>
        <tr><td>"Sensor Failure"</td><td>Check sensor lead is fully seated and the connector is clean and dry.</td></tr>
        <tr><td>Display blank</td><td>Confirm mains power and battery charge, then restart the unit.</td></tr>
        <tr><td>No reading</td><td>Reposition the probe and check patient contact.</td></tr>
      </table>
    </div>
  </div>

  <div class="page page--right">
    <div class="abs body-text" style="left:9px;top:14px;width:191px">
      <p class="lead" style="color:var(--red)">No Body Reads the User Manual, so now what!</p>
      <p>I don't and in all likelihood neither do you.</p>
      <p>We don't think it was ever meant to be read – it's a Reference Manual and professionals in healthcare have been using Reference Manuals for many years.</p>
      <p class="lead" style="margin-top:4px">So how can these Reference Documents make a difference?</p>
      <p>We believe that by focusing on one aspect of the Manufacturers Instruction Manual The User Troubleshooting Guide</p>
      <p>Largely driven by the culture of litigation in the USA, most manufacturers have developed robust data and error logging systems. This has allowed them to create very useful failure indicators, when used in conjunction with the <b>USER Troubleshooting Guide in the Manufacturers Reference Document aka User Manual, allows staff to:</b></p>
      <ul class="ticklist">
        <li>Accurately identify the problems</li>
        <li>Establish the possible cause – User or Technical Issue</li>
        <li>Offer suggested solutions which can be actioned at the point-of-care</li>
      </ul>
      <p>Our experience has been that most USE issues are the same problems repeated over and over. In many cases irrespective of the make or model of the device. User troubleshooting is a skill which can be taught and harnessed and this allows medical and nursing staff to gain confidence and real experience.</p>
      <p>Searchable pdf User Manuals allow staff to find the information they need within seconds and universal access to these manuals throughout the organisation allows management, education, and suppliers to grow these skills.</p>
    </div>

    <aside class="abs benefits">
      <h3>IMMEDIATE BENEFITS TO USING THE USER MANUAL LIBRARY</h3>
      <ul>
        <li><b>Standardised Access</b></li>
        <li>to all your hospitals Medical Equipment User Manuals throughout the various Departments, Buildings and Trusts.</li>
        <li><b>Inform e-mail support</b> via the Document Request Tab to any Biomed or member of staff – they will get feedback regarding their request</li>
        <li><b>Simple Set up</b> as quick as you can get the IT Department to place a link on your hospital Intranet.</li>
        <li><b>No Administrative Burden</b> or increase in staff work load to keep it up-to-date. We do all the work.</li>
        <li><b>One of the most valuable components of the Manufacturers Reference Manual is the User Troubleshooting Guide</b></li>
        <li>This is part of the process of getting Make and Model experience – working through and "fixing" user issues helping Clinicians in their understanding of the devices they use everyday.</li>
      </ul>
    </aside>

    <div class="abs cycle-box" style="left:73px;top:330px;width:94px;height:48px">Device Educators focus on issues identified by "No Fault Found" Metric</div>
    <div class="abs cycle-box" style="left:273px;top:330px;width:100px;height:52px">Staff training includes basic troubleshooting related to "No Fault Found" metric as per the Biomed Equipment database</div>
    <div class="abs cycle-box" style="left:273px;top:410px;width:100px;height:52px">Biomedical Services measure and report "No Fault Found" to Device Trainers and Safety &amp; Quality</div>
    <div class="abs cycle-box" style="left:73px;top:404px;width:94px;height:66px">Safety &amp; Quality can now measure the effectiveness of Medical Device Training – safety improvements can be supported with additional funding</div>

    <svg class="abs" style="left:178px;top:340px;width:86px;height:130px" viewBox="0 0 86 130" aria-hidden="true">
      <defs><marker id="tipCycle" markerWidth="7" markerHeight="7" refX="3.5" refY="3.5" orient="auto"><path d="M0,0 L7,3.5 L0,7 z" fill="#f08b1c"/></marker></defs>
      <g stroke="#f08b1c" stroke-width="5" fill="none" marker-end="url(#tipCycle)">
        <path d="M14,38 A34,34 0 0 1 60,24"/>
        <path d="M74,44 A34,34 0 0 1 72,88"/>
        <path d="M62,102 A34,34 0 0 1 22,100"/>
        <path d="M10,86 A34,34 0 0 1 8,52"/>
      </g>
    </svg>

    <p class="abs foot-band">"No Fault Found" is an objective outcome of a device reported as having a fault and sent for repair, with no technical issue established – without focusing on an individual's ability or competence</p>
  </div>
</section>

</body>
</html>
```